Letterhead & Email Signature Design

Kindly assist redesign this letterhead as well as the Email signature. I have uploaded the current designs that needs some new look

```html
<!DOCTYPE html>
<html lang="en">
<head>
<meta charset="utf-8">
<title>Thato Kgosi Inc. – Letterhead &amp; Email Signature</title>
<link href="https://fonts.googleapis.com/css2?family=Lato:wght@300;400;700;900&display=swap" rel="stylesheet">
<style>
  :root{
    --ink:#1d1d1f;
    --body:#4a4a4a;
    --logo-grey:#939497;
    --rule:#b8b8b8;
    --band:#2a2a2b;
    --blue:#2a4d9b;
    --link:#6fa8e8;
    --paper:#ffffff;
    --sig-bg:#efeff0;
  }
  *{margin:0;padding:0;box-sizing:border-box}
  html,body{width:680px;height:1200px;overflow:hidden;background:var(--paper)}
  body{font-family:"Lato",sans-serif;color:var(--ink);position:relative}
  .abs{position:absolute}

  /* header */
  .brand-frame{left:75px;top:40px;width:252px;height:125px;border:1px solid var(--ink)}
  .brand-block{left:87px;top:0;width:228px;height:154px;background:var(--logo-grey);display:flex;align-items:center;justify-content:center}
  .brand-name{color:#fff;font-weight:400;font-size:40px;letter-spacing:1px}
  .practice{left:330px;width:278px;top:64px;text-align:center;font-size:13.2px;font-weight:700;white-space:nowrap}
  .practice .soft{color:var(--blue);font-weight:400}
  .practice .bar{font-weight:400}
  .reg{left:330px;width:278px;top:80px;text-align:center;font-size:11px;font-weight:700}
  .directors{left:330px;width:278px;top:106px;text-align:center;font-size:6.3px;line-height:8px;text-transform:uppercase}

  /* recipient */
  .recipient{left:86px;top:229px;font-size:7.6px;line-height:11.5px}
  .recipient .to{font-weight:700;font-size:9px}
  .recipient .name{font-size:9px;font-weight:700;color:#2b2b2b;margin-top:2px}
  .recipient .addr{margin-top:6px}
  .date{right:89px;top:282px;font-size:7.8px}
  .date b{font-size:8.6px}
  .divider{left:86px;top:310px;width:508px;height:1px;background:var(--rule)}

  /* letter body */
  .salutation{left:85px;top:328px;font-size:10px}
  .copy{left:86px;width:508px;font-size:8.6px;line-height:15.5px;color:var(--body);text-align:justify;hyphens:auto}
  .p1{top:347px}
  .p2{top:541px}
  .p3{top:635px}
  .points{left:128px;top:476px;font-size:8.6px;line-height:14.5px;color:var(--body);list-style:none}
  .points li::before{content:"•";margin-right:4px;color:var(--ink)}
  .signature-mark{left:86px;top:686px;width:86px;height:12px;background:linear-gradient(90deg,#cfcfcf,#e8e8e8);border-radius:6px}
  .closing{left:86px;top:700px;font-size:8.6px;line-height:13px}
  .closing b{font-weight:700}

  /* footer band */
  .footer-band{left:0;top:886px;width:680px;height:67px;background:var(--band);color:#f0f0f0}
  .footer-address{position:absolute;left:86px;top:18px;font-size:8.8px;line-height:10.8px;font-weight:300;text-transform:uppercase}
  .footer-contact{position:absolute;left:508px;top:18px;font-size:8.8px;line-height:10.8px;font-weight:300}
  .footer-contact b{font-weight:700}
  .footer-contact .mail{color:var(--link)}

  /* email signature */
  .sig-panel{left:0;top:973px;width:680px;height:207px;background:radial-gradient(ellipse at 30% 85%,#dcdcdd 0%,rgba(239,239,240,0) 45%),radial-gradient(ellipse at 75% 80%,#e0e0e1 0%,rgba(239,239,240,0) 45%),var(--sig-bg)}
  .sig-base{left:0;top:1180px;width:680px;height:20px;background:var(--band)}
  .sig-tab{left:94px;top:973px;width:79px;height:56px;background:var(--band)}
  .sig-badge{left:77px;top:1010px;width:114px;height:114px;border-radius:50%;background:var(--logo-grey);border:3px solid #fafafa;box-shadow:0 0 0 1px #dedede;display:flex;align-items:center;justify-content:center}
  .sig-badge span{color:#fff;font-size:23px;font-weight:400}
  .sig-practice{left:30px;width:186px;top:1130px;text-align:center;font-size:7.8px;line-height:9.8px;color:#333}
  .sig-person{left:232px;top:1035px;font-size:17px;color:#333}
  .sig-firm{left:231px;top:1054px;font-size:26px;font-weight:900;color:var(--ink);letter-spacing:-.5px}
  .sig-role{left:232px;top:1082px;font-size:15px;font-weight:300;color:#333}
  .sig-underline{left:233px;top:1106px;width:87px;height:1px;background:var(--ink)}
  .social{left:232px;top:1117px;display:flex;gap:5px}
  .social i{display:block;width:15px;height:15px;border-radius:50%;background:var(--band)}
  .sig-split{left:386px;top:1056px;width:1px;height:61px;background:var(--ink)}
  .sig-contacts{left:406px;top:0;font-size:7.9px;color:#333}
  .row{position:absolute;left:0;display:flex;gap:7px;white-space:nowrap;line-height:9.8px}
  .row svg{flex:none;margin-top:1px}
  .row .upper{text-transform:uppercase}
</style>
</head>
<body>

<!-- Letterhead header -->
<div class="abs brand-frame"></div>
<div class="abs brand-block"><span class="brand-name">TK Inc.</span></div>

<div class="abs practice">ATTORNEYS <span class="bar">|</span>&nbsp; <span class="soft">CONVEYANCERS</span>&nbsp; <span class="bar">|</span> NOTARIES</div>
<div class="abs reg">Reg. No.: 2011/004518/21</div>
<div class="abs directors">Directors: R P Dube B. Proc LLB (Hons) &nbsp;|&nbsp; L Kgosi (LLB)<br>Consultant: NT Kgosi</div>

<!-- Recipient -->
<div class="abs recipient">
  <div class="to">TO</div>
  <div class="name">Karen Doyle</div>
  <div>Position / Company Name</div>
  <div class="addr">28th Streat Name, City Name<br>Location Name,US</div>
</div>
<div class="abs date"><b>DATE :</b> 18 August 2021</div>
<div class="abs divider"></div>

<!-- Letter body -->
<div class="abs salutation">Dear Sir</div>
<p class="abs copy p1">There are many variations of passages of Lorem Ipsum available, but the majority have suffered alteration in some for injected humour.But I must explain to you how all this mistaken ienouncing pleasure and praising pain was born and I will give you a complete account of the systd expound the actual teachings of the great explorer of the truth, the master-builder of humppiness. No one rejects, dislikes, or avoids pleasure itself, because it is pleasure, but because those who do not know how to pursue pleasure rationally encounter consequences that are extremely painful. Nor again is there anyone who loves or pursues or desires to obtain pain of itself, because it is pain, but because occasionally circumstances occur in which toil and pain can procure him some great pleasure. To take a trivial example, which of us ever undertakes</p>

<ul class="abs points">
  <li>Nunc rhoncus quam ac sapien pulvinar, vitae convallis mi porttitor.</li>
  <li>Phasellus placerat tortor maximus, faucibus magna nec, consectetur nisi.</li>
  <li>Variations of passages of Lorem Ipsum available, but</li>
</ul>

<p class="abs copy p2">There are many variations of passages of Lorem Ipsum available, but the majority have suffered alteration in some for injected humour.But I must explain to you how all this mistaken ienouncing pleasure and praising pain was born and I will give you a complete account of the systd expound the actual teachings of the great explorer of the truth, the master-builder of humppiness. No one rejects, dislikes, or avoids pleasure itself, because it is pleasure, but because those who do not know how to pursue pleasure rationally encounter consequences that are extremely painful.</p>

<p class="abs copy p3">Nor again is there anyone who loves or pursues or desires to obtain pain of itself, because it is pain, but because occasionally circumstances occur in which toil and pain can procure him some great pleasure. To take a trivial example, which of us ever undertakes</p>

<div class="abs signature-mark" role="img" aria-label="Handwritten signature of Dirk Vollmer"></div>
<div class="abs closing">Sincerely<br><b>Dirk Vollmer</b></div>

<!-- Letterhead footer -->
<div class="abs footer-band">
  <div class="footer-address">The Acacia Office Park &nbsp;|&nbsp; Ground Floor, Building B<br>41 Marula Street &nbsp;|&nbsp; Garsfontein &nbsp;|0042</div>
  <div class="footer-contact"><b>THATO KGOSI INC.</b><br><span class="mail">Info@thatokgosi.co.za</span><br>Tel: 012 345 6701<br>Fax: 012 345 6702</div>
</div>

<!-- Email signature -->
<div class="abs sig-panel"></div>
<div class="abs sig-base"></div>
<div class="abs sig-tab"></div>
<div class="abs sig-badge"><span>TK Inc.</span></div>
<div class="abs sig-practice">ATTORNEYS| CONVEYANCERS |NOTARIES<br>REG. NO.: 2011/004518/21</div>

<div class="abs sig-person">L. Kgosi</div>
<div class="abs sig-firm">TK Inc.</div>
<div class="abs sig-role">Director (LLB)</div>
<div class="abs sig-underline"></div>
<div class="abs social" aria-label="Social profiles"><i></i><i></i><i></i><i></i></div>

<div class="abs sig-split"></div>

<div class="abs sig-contacts">
  <div class="row" style="top:1051px">
    <svg width="10" height="10" viewBox="0 0 24 24"><path fill="#222" d="M6.6 10.8a15.2 15.2 0 0 0 6.6 6.6l2.2-2.2c.3-.3.7-.4 1-.2 1.1.4 2.3.6 3.6.6.6 0 1 .4 1 1V20c0 .6-.4 1-1 1A17 17 0 0 1 3 4c0-.6.4-1 1-1h3.5c.6 0 1 .4 1 1 0 1.3.2 2.5.6 3.6.1.3 0 .7-.2 1z"/></svg>
    <span>Tel: 012 345 6701<br>Fax: 012 345 6702</span>
  </div>
  <div class="row" style="top:1086px">
    <svg width="10" height="9" viewBox="0 0 24 18"><rect x="0" y="0" width="24" height="18" fill="#222"/><path d="M1 1l11 9 11-9" stroke="#efeff0" stroke-width="2" fill="none"/></svg>
    <span>Info@thatokgosi.co.za</span>
  </div>
  <div class="row" style="top:1100px">
    <svg width="10" height="10" viewBox="0 0 24 24" fill="none" stroke="#222" stroke-width="2"><circle cx="12" cy="12" r="10"/><path d="M2 12h20M12 2c3 3 3 17 0 20M12 2c-3 3-3 17 0 20"/></svg>
    <span>urwebsitename.com</span>
  </div>
  <div class="row" style="top:1115px">
    <svg width="11" height="10" viewBox="0 0 24 22"><path fill="#222" d="M12 1 0 11h3v10h7v-7h4v7h7V11h3z"/></svg>
    <span class="upper">The Acacia Office Park | Ground Floor, Building B<br>41 Marula Street | Garsfontein |0042</span>
  </div>
</div>

</body>
</html>
```